Business Card Design

We need a business card design for our new expansion based in Bloomfield Hills, Michigan. Our company is Quiet Harbor Institute & Wellness Center. Our Academy teaches individuals of all ages and professions to live from their soul. We teach intuitive development, meditation and mindfulness; shamanic healing. And ourr healing center provides holistic services. We offer certification programs that support the ethical practices of Intuitive professionals. Our team of Intuitive Practitioners includes: doctors, psychologists, chiropractor, soul retrievers, mediums, etc who all balance their knowledge with intuitive wisdom.

We want our symbol to be the Blue Morpho Buttefly and the colors on the card to complement it. We want to communicate inspiration, healing and empowerment. Thank you
Updates

Industry/Entity Type

Business

Contact Information for Business Card

Dana Orwick
Medium. Author. Soul Retriever.
Founder, Quiet Harbor

Quiet Harbor

19 North Cedar Mill Drive Suite 100
Fernwood Heights, MI 48517
248-603-7418

www.danaorwick.example

Requirements
Must have
• blue morpho butterfly

```html
<!DOCTYPE html>
<html lang="en">
<head>
<meta charset="utf-8">
<title>Quiet Harbor – Business Card</title>
<link href="https://fonts.googleapis.com/css2?family=Lato:wght@400;700&family=Petit+Formal+Script&display=swap" rel="stylesheet">
<style>
  :root {
    --backdrop: #e6e7ea;
    --card: #ffffff;
    --ink: #151515;
    --accent: #3a48a8;
    --morpho: #2a86dc;
    --shadow: rgba(0, 0, 0, 0.18);
  }
  * { box-sizing: border-box; margin: 0; padding: 0; }
  html, body {
    width: 1200px;
    height: 900px;
    overflow: hidden;
    background: var(--backdrop);
    font-family: "Lato", Arial, sans-serif;
    color: var(--ink);
  }
  .sheet {
    width: 1200px;
    height: 900px;
    display: flex;
    flex-direction: column;
    align-items: center;
    justify-content: center;
    gap: 40px;
  }
  .card {
    width: 700px;
    height: 400px;
    background: var(--card);
    box-shadow: 0 6px 20px var(--shadow);
    display: flex;
    flex-direction: column;
    align-items: center;
    text-align: center;
  }

  /* Front */
  .card--front { justify-content: center; }
  .brand-mark {
    width: 64px;
    height: 64px;
    border-radius: 50%;
    background: var(--morpho);
    margin-bottom: 22px;
  }
  .brand-name {
    font-weight: 400;
    font-size: 64px;
    line-height: 1;
    color: var(--ink);
    letter-spacing: 1px;
  }
  .tagline {
    margin-top: 14px;
    font-size: 22px;
    color: var(--accent);
    letter-spacing: 0.3px;
  }

  /* Back */
  .card--back { justify-content: center; padding: 0 30px; }
  .brand-mark--small {
    width: 40px;
    height: 40px;
    margin-bottom: 10px;
  }
  .brand-name--small { font-size: 38px; }
  .person-name {
    margin-top: 14px;
    font-family: "Petit Formal Script", cursive;
    font-size: 34px;
    color: var(--accent);
    line-height: 1.2;
  }
  .person-role {
    margin-top: 4px;
    font-size: 19px;
  }
  .contact {
    margin-top: 18px;
    list-style: none;
    font-size: 19px;
    line-height: 1.45;
  }
  .contact__label {
    font-weight: 700;
    color: var(--accent);
  }
</style>
</head>
<body>
  <main class="sheet">
    <section class="card card--front" aria-label="Business card front">
      <span class="brand-mark" aria-hidden="true"></span>
      <h1 class="brand-name">Quiet Harbor</h1>
      <p class="tagline">Guiding Quiet Strength for Purposeful Everyday Living</p>
    </section>

    <section class="card card--back" aria-label="Business card back">
      <span class="brand-mark brand-mark--small" aria-hidden="true"></span>
      <h2 class="brand-name brand-name--small">Quiet Harbor</h2>
      <p class="person-name">Dana Orwick</p>
      <p class="person-role">Medium, Author, Soul Retriever, Founder of Quiet Harbor.</p>
      <ul class="contact">
        <li><span class="contact__label">Phone:</span> 248-603-7418</li>
        <li><span class="contact__label">Website:</span> www.danaorwick.example</li>
        <li><span class="contact__label">Address:</span> 19 North Cedar Mill Drive Suite 100 Fernwood Heights, MI 48517</li>
      </ul>
    </section>
  </main>
</body>
</html>
```